Q5 Pops (CBD candy infused with Delta-8)

The proposed logo are two pool table balls. One is a D and the other is an 8, its a brand and we need a label for Gummy human treats. This treats are being infused with Delt-8. I i will upload examples only. The example is of the type of labels needed (package and label for bottle)

Target Market(s)

Your professionals

Font styles to use
Sans Serif

Requirements
Must have
• Youthful look
Nice to have
• Consider using the Delta symbol instead of the D.
Also, I provided a sample of a label that's used on two type of packages.

```html
<!DOCTYPE html>
<html lang="en">
<head>
<meta charset="utf-8">
<title>Q5 Pops – CBD Gummy Candy Label</title>
<link href="https://fonts.googleapis.com/css2?family=League+Spartan:wght@600;700;800&family=Roboto+Condensed:wght@600&display=swap" rel="stylesheet">
<style>
  :root {
    --bg: #f2f2f2;
    --green: #1f8a2c;
    --green-dark: #17731f;
    --pale-blue: #dcebef;
    --white: #ffffff;
    --ink: #111111;
    --grey-text: #5f6b66;
    --candy-teal: #1fb8b8;
    --candy-red: #ef4f5a;
    --candy-orange: #f98a12;
  }
  * { margin: 0; padding: 0; box-sizing: border-box; }
  html, body {
    width: 1200px; height: 989px; overflow: hidden;
    background: var(--bg);
    font-family: "League Spartan", "Futura", sans-serif;
  }
  .canvas { position: relative; width: 1200px; height: 989px; }
  .label {
    position: absolute; left: 320px; top: 110px;
    width: 560px; height: 770px;
    background: var(--pale-blue);
    overflow: hidden;
  }
  .top-band {
    position: absolute; left: 0; top: 0; width: 100%; height: 70px;
    background: var(--green);
    display: flex; align-items: center; justify-content: center;
    color: var(--white); font-weight: 700; font-size: 21px; letter-spacing: 4px;
  }
  .halo {
    position: absolute; left: 50px; top: 190px;
    width: 460px; height: 460px; border-radius: 50%;
    background: var(--white);
  }
  .bottom-band { position: absolute; left: 0; top: 560px; width: 560px; height: 210px; }
  .brand {
    position: absolute; left: 0; top: 120px; width: 100%;
    display: flex; flex-direction: column; align-items: center;
  }
  .brand-dot {
    width: 110px; height: 110px; border-radius: 50%;
    background: var(--ink); margin-bottom: 14px;
  }
  .brand-name {
    font-weight: 800; font-size: 96px; line-height: 1; color: var(--ink);
    letter-spacing: 1px;
  }
  .infused {
    position: absolute; left: 0; top: 385px; width: 100%; text-align: center;
    font-weight: 700; font-size: 33px; color: var(--grey-text); letter-spacing: 1px;
  }
  .candy-art {
    position: absolute; left: 70px; top: 435px; width: 420px; height: 215px;
    border-radius: 108px;
    background: linear-gradient(90deg, var(--candy-teal) 0%, var(--candy-red) 35%, var(--candy-orange) 75%);
  }
  .dose {
    position: absolute; left: 0; top: 660px; width: 100%; text-align: center;
    color: var(--white); font-weight: 800; font-size: 42px; line-height: 1;
  }
  .dose small { font-size: 32px; }
  .product-type {
    position: absolute; left: 0; top: 703px; width: 100%; text-align: center;
    color: var(--white); font-weight: 700; font-size: 27px; letter-spacing: 1.5px;
  }
  .net-weight {
    position: absolute; left: 185px; top: 738px; width: 190px; height: 52px;
    background: var(--white); border-radius: 22px;
    display: flex; align-items: flex-start; justify-content: center; padding-top: 8px;
    font-family: "Roboto Condensed", "Arial Narrow", sans-serif; font-weight: 600;
    font-size: 25px; color: var(--ink);
  }
</style>
</head>
<body>
<div class="canvas">
  <div class="label">
    <div class="top-band">PREMIUM CBD EDIBLES</div>
    <div class="halo"></div>
    <svg class="bottom-band" viewBox="0 0 560 210" aria-hidden="true">
      <path d="M0 10 Q280 -6 560 10 L560 210 L0 210 Z" fill="var(--green)"/>
      <path d="M0 176 Q280 160 560 176" stroke="var(--white)" stroke-width="3" fill="none"/>
    </svg>
    <div class="brand">
      <div class="brand-dot"></div>
      <div class="brand-name">Q5 Pops</div>
    </div>
    <div class="infused">DELTA-8 INFUSED</div>
    <div class="candy-art" role="img" aria-label="Illustration of three glossy gummy candy balls in teal, red and orange"></div>
    <div class="dose">75<small>MG</small></div>
    <div class="product-type">CBD GUMMY CANDY</div>
    <div class="net-weight">NET WT 40G</div>
  </div>
</div>
</body>
</html>
```